Software company seeks new website design

We are a UK based company called Harbourlight Systems. We build software which helps other businesses to manage their accounts and company finances. All of our clients enjoy full telephone based support as well as access to our software. So, we like to think that we are combining the best accountancy software in the world with a friendly human touch.
We need our homepage completely redesigned. At the moment we have two products which we want to highlight. They are called 'Quick Ledger' (which you can view at www.quickledgr.example) and Tally Beacon.
*VERY IMPORTANT!* We would like the focus of the site to be on our latest new product - Tally Beacon.
We have included a variety of files to help you out, including graphics and some text. Our target audience is medium and large UK based companies who are interested in finding a cost effective and intelligent accountancy solution.
The main call to action on the home page should be EITHER 'learn more', 'find out more' or 'arrange a free demonstration'. If you are unsure about what the text should say then you can use 'Lorem Ipsum'.
Site that we like include:
http://brindlevault.example/
http://www.norvanta.example/
Thank you for viewing. We promise to give constructive feedback to every person who submits a design. Thank you so much. Good luck to you!
IMPORTANT UPDATE: THE PIXEL MARKET WEBSITE KEEPS LOGGING ME OUT WHEN I TRY TO ADD FEEDBACK. I HAVE CONTACTED TECHNICAL SUPPORT AND I'M WAITING FOR A RESOLUTION. I SHALL OFFER FEEDBACK TO EVERY ONE OF YOU AS SOON AS THE PIXEL MARKET WEBSITE IS WORKING PROPERLY
ANOTHER IMPORTANT UPDATE: I SAID ABOVE THAT I'D LIKE THE FOCUS ON THE SITE TO BE ON THE PRODUCT 'TALLY BEACON' - NOT QUICK LEDGER. ONE PERSON HAS ALREADY WASTED TIME BY NOT FOLLOWING THAT INSTRUCTION. SO, ONCE AGAIN - PLEASE MAKE THE FOCUS OF THE SITE ON TALLY BEACON - NOT QUICK LEDGER. THANKS FOLKS. I APPRECIATE YOU BEING HERE.
Reason: Sorry folks, there was a problem with the system which prevented me from leaving any feedback. That problem has now been resolved, however, the guy who is making the final decision is away for a few days. Thank you for everything so far. There's some really great designs so far. Every design will be checked out and given a comment. You have my word.
Reason: Sorry folks, it's been an incredibly busy week and we haven't had time to check the designs out.

```html
<!DOCTYPE html>
<html lang="en">
<head>
<meta charset="utf-8">
<title>Tally Beacon – Unlock the potential of your ERP system</title>
<link href="https://fonts.googleapis.com/css2?family=Signika:wght@400;600&family=Arimo:ital,wght@0,400;0,700;1,700&display=swap" rel="stylesheet">
<style>
:root{
  --teal:#0f7a9e;
  --teal-dark:#0b6485;
  --cyan:#19b8d6;
  --cyan-light:#3fcbe3;
  --blue-text:#1478a8;
  --heading:#2b2b2b;
  --body:#333;
  --icon-blue:#1e90e8;
  --footer:#0e6f95;
}
*{box-sizing:border-box;margin:0;padding:0}
html,body{width:973px;height:1200px;overflow:hidden;background:#fff}
body{position:relative;font-family:"Arimo",Arial,sans-serif;color:var(--body)}
a{color:inherit;text-decoration:none}
.abs{position:absolute}

.site-header{left:0;top:0;width:973px;height:101px;background:linear-gradient(#f2f3f3,#e7e9e9)}
.brand{left:97px;top:24px;display:flex;align-items:center;gap:10px}
.brand-mark{width:56px;height:54px;background:var(--cyan)}
.brand-name{font-family:"Signika",sans-serif;font-size:27px;font-weight:400;color:#356a86;line-height:1}
.brand-tag{font-size:9px;color:#555;margin-top:4px}
.phone{left:685px;top:30px;width:187px;height:44px;border-radius:22px;background:#f6f6f6;box-shadow:0 1px 3px rgba(0,0,0,.15);display:flex;align-items:center;padding-left:12px;gap:14px}
.phone-num{font-family:"Signika",sans-serif;font-size:17px;color:#444;font-weight:600}

.teal-band{left:0;top:101px;width:973px;height:414px;background:radial-gradient(ellipse at center,#1584aa,var(--teal-dark))}
.main-nav{left:97px;top:101px;width:779px;height:34px;background:linear-gradient(var(--cyan-light),var(--cyan));border-radius:0 0 6px 6px;display:flex}
.main-nav a{color:#fff;font-size:11px;font-weight:700;display:flex;align-items:center;justify-content:center;border-right:1px solid rgba(255,255,255,.3)}
.main-nav a:last-child{border-right:none}

.hero{left:96px;top:160px;width:780px;height:292px;background:linear-gradient(90deg,#dfe9ee,#b9c7cf 30%,#3c4248 50%,#bac8d0 70%,#e2ecf1)}
.hero-arrow{top:120px}

.features{left:97px;top:474px;width:779px;height:77px;background:linear-gradient(#fff,#f1f2f2);border-radius:6px 6px 0 0;box-shadow:0 -2px 4px rgba(0,0,0,.08);display:flex}
.feature{flex:1;display:flex;align-items:center;padding:0 10px;border-right:1px solid #ddd;height:56px;margin-top:6px}
.feature:last-child{border-right:none}
.feature-icon{width:36px;height:34px;background:var(--icon-blue);display:flex;align-items:center;justify-content:center;flex:none}
.feature-text{flex:1;text-align:center;font-family:"Signika",sans-serif;font-size:13.5px;color:#333;line-height:1.15}
.feature-go{width:18px;height:18px;border-radius:50%;background:#c9c9c9;flex:none;display:flex;align-items:center;justify-content:center}
.feature:hover .feature-go{background:var(--cyan)}

.welcome{left:99px;top:571px;width:512px}
.welcome h1{font-family:"Signika",sans-serif;font-weight:600;font-size:17px;color:var(--heading)}
.welcome h1 span{color:var(--blue-text)}
.welcome h2{font-size:13px;color:var(--blue-text);font-weight:700;margin-top:16px}
.welcome h3{font-size:11px;color:var(--blue-text);font-weight:700;margin-top:1px}
.welcome .lead{font-size:11px;line-height:14px;margin-top:13px}
.welcome .detail{font-size:9px;line-height:11.5px;margin-top:11px}
.divider{left:616px;top:571px;width:1px;height:168px;background:#e3e3e3}
.testimonials{left:627px;top:571px;width:253px}
.testimonials h2{font-family:"Signika",sans-serif;font-weight:600;font-size:17px;color:var(--heading)}
.t-nav{position:absolute;right:12px;top:1px;display:flex;gap:2px}
.t-nav span{width:19px;height:18px;background:#222;display:flex;align-items:center;justify-content:center}
.testimonials blockquote{font-size:9px;font-style:italic;font-weight:700;line-height:14.6px;color:#333;margin-top:24px}
.testimonials cite{display:block;text-align:right;font-size:11px;color:var(--blue-text);font-weight:700;font-style:italic;margin-top:12px}

.promo{left:0;top:766px;width:973px;height:90px;background:#fff;box-shadow:0 -6px 10px -8px rgba(0,0,0,.25),0 6px 10px -8px rgba(0,0,0,.25);display:flex;align-items:center;justify-content:center;font-family:"Signika",sans-serif;font-weight:600;font-size:25px;color:var(--cyan);letter-spacing:.5px;gap:22px}
.promo:hover{background:#f7fcfd}
.promo .partner{color:var(--teal)}

.card{top:882px;width:243px;height:219px;background:#fff;box-shadow:0 0 3px rgba(0,0,0,.25)}
.card-img{margin:2px;height:118px}
.card h3{font-family:"Signika",sans-serif;font-weight:600;font-size:14.5px;letter-spacing:.5px;color:#222;margin:10px 0 0 9px}
.card p{font-size:9.6px;line-height:14.6px;margin:6px 10px 0 9px;color:#333}

.site-footer{left:0;top:1142px;width:973px;height:58px;background:var(--footer)}
.footer-copy{left:97px;top:25px;font-size:9px;color:#fff}
.social{left:779px;top:15px;display:flex;gap:4px}
.social span{width:27px;height:27px;border-radius:50%;background:#1e5ea3;border:2px solid #dfe8f0}
</style>
</head>
<body>

<header class="site-header abs">
  <div class="brand abs">
    <div class="brand-mark"></div>
    <div>
      <div class="brand-name">Tally Beacon</div>
      <div class="brand-tag">Unlock the potential of your ERP system</div>
    </div>
  </div>
  <a class="phone abs" href="tel:02075550148" aria-label="Call us to arrange a free demonstration">
    <svg width="30" height="26" viewBox="0 0 30 26" aria-hidden="true"><path d="M3 9c0-5 24-5 24 0v3h-6V9H9v3H3z" fill="#333"/><rect x="6" y="13" width="18" height="11" rx="2" fill="#444"/><circle cx="15" cy="18" r="3" fill="#ddd"/></svg>
    <span class="phone-num">0207 555 0148</span>
  </a>
</header>

<div class="teal-band abs"></div>

<nav class="main-nav abs">
  <a href="#" style="width:97px">HOME</a>
  <a href="#" style="width:121px">ABOUT US</a>
  <a href="#" style="width:146px">HOW IT WORKS</a>
  <a href="#" style="width:134px">TESTIMONIES</a>
  <a href="#" style="width:139px">OUR PROMISE</a>
  <a href="#" style="width:142px">CONTACT US</a>
</nav>

<div class="hero abs" role="img" aria-label="Photo of a team of business people standing in a bright office">
  <svg class="hero-arrow abs" style="left:14px" width="30" height="44" viewBox="0 0 30 44" aria-hidden="true"><path d="M26 2 4 22l22 20" fill="none" stroke="var(--teal)" stroke-width="3"/></svg>
  <svg class="hero-arrow abs" style="right:14px" width="30" height="44" viewBox="0 0 30 44" aria-hidden="true"><path d="M4 2l22 20L4 42" fill="none" stroke="var(--teal)" stroke-width="3"/></svg>
</div>

<section class="features abs" aria-label="Find out more">
  <a class="feature" href="#" aria-label="Find out more: forecasting the future just got easier">
    <div class="feature-icon"><svg width="22" height="18" viewBox="0 0 22 18" aria-hidden="true"><path d="M2 16h18M3 13l5-5 4 3 7-7M15 4h4v4" fill="none" stroke="#fff" stroke-width="2"/></svg></div>
    <div class="feature-text">Forecasting the future<br>just got easier</div>
    <div class="feature-go"><svg width="8" height="10" viewBox="0 0 8 10"><path d="M2 1l4 4-4 4" fill="none" stroke="#fff" stroke-width="2"/></svg></div>
  </a>
  <a class="feature" href="#" aria-label="Find out more: low risk solution">
    <div class="feature-icon"><svg width="22" height="20" viewBox="0 0 22 20" aria-hidden="true"><rect x="2" y="4" width="14" height="14" fill="none" stroke="#fff" stroke-width="2"/><path d="M5 10l4 4 11-12" fill="none" stroke="#fff" stroke-width="3"/></svg></div>
    <div class="feature-text">Low Risk Solution</div>
    <div class="feature-go"><svg width="8" height="10" viewBox="0 0 8 10"><path d="M2 1l4 4-4 4" fill="none" stroke="#fff" stroke-width="2"/></svg></div>
  </a>
  <a class="feature" href="#" aria-label="Find out more: keep your finger on the pulse of your business">
    <div class="feature-icon"><svg width="20" height="20" viewBox="0 0 20 20" aria-hidden="true"><circle cx="10" cy="10" r="6" fill="none" stroke="#fff" stroke-width="2"/><circle cx="10" cy="10" r="2" fill="#fff"/></svg></div>
    <div class="feature-text">Keep your finger on the<br>pulse of your business</div>
    <div class="feature-go"><svg width="8" height="10" viewBox="0 0 8 10"><path d="M2 1l4 4-4 4" fill="none" stroke="#fff" stroke-width="2"/></svg></div>
  </a>
</section>

<section class="welcome abs">
  <h1>Welcome to <span>TallyBeacon</span></h1>
  <h2>An innovative service that solves your reporting problems</h2>
  <h3>TallyBeacon is a complete solution to the perennial problem of a lack of information</h3>
  <p class="lead">TallyBeacon is a service from Harbourlight Systems that provides you with all the information you require from your operational systems.</p>
  <p class="detail">The lack of meaningful, timely and accurate information is an age-old problem TallyBeacon provides you with all the reports you need, when you need it and, in the format you specify, all at a fixed monthly price. Much more than a software tool, Tally Beacon is a complete reporting service. Simply put, would you prefer to purchase the latest labour saving kitchen device or have a meal served to you on a plate? TallyBeacon is exactly that - service on a plate. You order what you wish and we serve it to you - online and in real time.</p>
</section>

<div class="divider abs"></div>

<aside class="testimonials abs">
  <h2>Testimonials</h2>
  <div class="t-nav">
    <span><svg width="6" height="8" viewBox="0 0 6 8"><path d="M5 0v8L0 4z" fill="#fff"/></svg></span>
    <span><svg width="6" height="8" viewBox="0 0 6 8"><path d="M1 0v8l5-4z" fill="#fff"/></svg></span>
  </div>
  <blockquote>At vero eos et accusamus et iusto odio dignissimos ducimus qui blanditiis praesentium voluptatum deleniti atque corruptvoluptatum deleniti atque corrupti&nbsp; deleniti atque corrupti s qui blanditiis praesentium voluptatum deleniti atque corruptvoluptatum deleniti atque corrupti&nbsp; deleniti atque corrupti</blockquote>
  <cite>- Marcus</cite>
</aside>

<a class="promo abs" href="#" aria-label="Find out more about unlocking the potential of your Corvello system">
  <span>UNLOCK THE POTENTIAL&nbsp; OF YOU</span>
  <span class="partner">Corvello</span>
  <span>SYSTEM</span>
</a>

<article class="card abs" style="left:99px">
  <div class="card-img" role="img" aria-label="Blue 3D business charts and graphs" style="background:linear-gradient(160deg,#9fd0f2,#2f7fd6 60%,#1b5eb8)"></div>
  <h3>ALL THE REPORTS YOU NEED...</h3>
  <p>There is no limit to the number of reports your users can request. They can have as many as they wish and all requests are turned around</p>
</article>
<article class="card abs" style="left:366px">
  <div class="card-img" role="img" aria-label="Businesswoman writing notes at a desk" style="background:linear-gradient(100deg,#8e9a9c,#5d6a6e 55%,#2a2f33)"></div>
  <h3>WHEN YOU NEED THEM</h3>
  <p>If you need a new report or require a new one built, just call our dedicated BeaconLine. One of our friendly consultants will build your new report for you online in real time.</p>
</article>
<article class="card abs" style="left:633px">
  <div class="card-img" role="img" aria-label="Close-up of coloured file folders on a shelf" style="background:linear-gradient(100deg,#c9b27a,#e8c238 35%,#8a3f82 60%,#d9d4cf)"></div>
  <h3>ALL THE REPORTS YOU NEED...</h3>
  <p>All reports for formatted to publication quality with your logo, fonts, colours etc. In addition to reports forprinting or to bedistributedas pdfs, our service includes dashboards built to your specifications</p>
</article>

<footer class="site-footer abs">
  <p class="footer-copy abs">© Copyright 2012 TallyBeacon | All rights reserved | Quick Ledger is a trading arm of Harbourlight Systems Ltd</p>
  <div class="social abs" aria-label="Social links">
    <span></span><span></span><span></span>
  </div>
</footer>

</body>
</html>
```